Bakery Business Cards

We are in need of business cards for our bakery business--something non-generic that reflects our business and will stand out. We are a wholesale bakery that primarily services in-store bakeries, casinos, schools, distributors, and fund-raising companies. The family business was founded in 1960. (www.marlowsovenworks.com)

```html
<!DOCTYPE html>
<html lang="en">
<head>
<meta charset="utf-8">
<title>Marlow's Ovenworks Business Cards</title>
<link href="https://fonts.googleapis.com/css2?family=Lora:wght@400;600&display=swap" rel="stylesheet">
<style>
  :root {
    --backdrop: #2b2b2d;
    --brand-blue: #1446c0;
    --brand-blue-light: #2a5fd3;
    --cream: #efe3d2;
    --cream-deep: #d9c3a8;
    --white: #ffffff;
  }
  * { margin: 0; padding: 0; box-sizing: border-box; }
  html, body {
    width: 1200px; height: 801px; overflow: hidden;
    background: var(--backdrop);
    font-family: "Lora", Georgia, serif;
  }
  .card {
    position: absolute; top: 246px;
    width: 540px; height: 309px;
    border-radius: 14px; overflow: hidden;
  }
  .card-front { left: 40px; }
  .card-back { left: 620px; }
  .card-art { position: absolute; inset: 0; width: 100%; height: 100%; }
  .brand-lockup {
    position: absolute; display: flex; flex-direction: column; align-items: center;
  }
  .brand-name {
    display: flex; align-items: center; gap: 10px;
    font-weight: 600; white-space: nowrap;
  }
  .brand-dot { width: 14px; height: 14px; border-radius: 50%; }
  .brand-tagline {
    font-weight: 600; letter-spacing: 2px; text-transform: uppercase; white-space: nowrap;
  }
  .card-front .brand-lockup { left: 0; right: 0; top: 114px; }
  .card-front .brand-name { font-size: 34px; color: var(--white); }
  .card-front .brand-dot { background: var(--white); }
  .card-front .brand-tagline { font-size: 15px; color: var(--white); margin-top: 6px; }
  .card-back .brand-lockup { left: 306px; right: 0; top: 56px; }
  .card-back .brand-name { font-size: 18px; color: var(--brand-blue); gap: 7px; }
  .card-back .brand-dot { background: var(--brand-blue); width: 9px; height: 9px; }
  .card-back .brand-tagline { font-size: 10px; color: var(--brand-blue); margin-top: 3px; letter-spacing: 1.5px; }
  .partner-badge {
    position: absolute; left: 410px; top: 128px;
    width: 70px; height: 70px; border-radius: 50%;
    border: 3px solid var(--brand-blue); background: rgba(255,255,255,0.85);
  }
  .contact-block {
    position: absolute; left: 38px; top: 62px; color: var(--white);
  }
  .person-name { font-size: 23px; font-weight: 600; letter-spacing: 0.5px; line-height: 1.25; }
  .person-title { font-size: 14px; margin-top: 2px; }
  .address { font-size: 13.5px; line-height: 1.5; margin-top: 20px; }
  .contact-list { list-style: none; margin-top: 18px; font-size: 13.5px; }
  .contact-list li { display: flex; align-items: center; gap: 9px; line-height: 1.6; }
  .contact-list svg { width: 12px; height: 12px; flex: none; }
</style>
</head>
<body>

<section class="card card-front">
  <svg class="card-art" viewBox="0 0 540 309" role="img" aria-label="Blue-tinted photo of pie slices on plates">
    <defs>
      <radialGradient id="frontTint" cx="50%" cy="45%" r="70%">
        <stop offset="0" stop-color="#2a5fd3"/>
        <stop offset="1" stop-color="#1446c0"/>
      </radialGradient>
    </defs>
    <rect width="540" height="309" fill="url(#frontTint)"/>
  </svg>
  <div class="brand-lockup">
    <div class="brand-name"><span class="brand-dot"></span>Marlow's Ovenworks</div>
    <div class="brand-tagline">Since 1960</div>
  </div>
</section>

<section class="card card-back">
  <svg class="card-art" viewBox="0 0 540 309">
    <defs>
      <linearGradient id="pieTone" x1="0" y1="0" x2="1" y2="1">
        <stop offset="0" stop-color="#e9d8c0"/>
        <stop offset="0.5" stop-color="#f4ece2"/>
        <stop offset="1" stop-color="#d9c3a8"/>
      </linearGradient>
    </defs>
    <rect width="540" height="309" fill="url(#pieTone)" role="img" aria-label="Photo of berry pie and a pie slice on a white plate"/>
    <path fill="#1446c0" d="M0 0 H300
      a6.18 6.18 0 0 1 0 12.36 a6.18 6.18 0 0 1 0 12.36 a6.18 6.18 0 0 1 0 12.36 a6.18 6.18 0 0 1 0 12.36 a6.18 6.18 0 0 1 0 12.36
      a6.18 6.18 0 0 1 0 12.36 a6.18 6.18 0 0 1 0 12.36 a6.18 6.18 0 0 1 0 12.36 a6.18 6.18 0 0 1 0 12.36 a6.18 6.18 0 0 1 0 12.36
      a6.18 6.18 0 0 1 0 12.36 a6.18 6.18 0 0 1 0 12.36 a6.18 6.18 0 0 1 0 12.36 a6.18 6.18 0 0 1 0 12.36 a6.18 6.18 0 0 1 0 12.36
      a6.18 6.18 0 0 1 0 12.36 a6.18 6.18 0 0 1 0 12.36 a6.18 6.18 0 0 1 0 12.36 a6.18 6.18 0 0 1 0 12.36 a6.18 6.18 0 0 1 0 12.36
      a6.18 6.18 0 0 1 0 12.36 a6.18 6.18 0 0 1 0 12.36 a6.18 6.18 0 0 1 0 12.36 a6.18 6.18 0 0 1 0 12.36 a6.18 6.18 0 0 1 0 12.36
      V309 H0 Z"/>
  </svg>

  <div class="brand-lockup">
    <div class="brand-name"><span class="brand-dot"></span>Marlow's Ovenworks</div>
    <div class="brand-tagline">Since 1960</div>
  </div>
  <div class="partner-badge" aria-label="Partner badge"></div>

  <div class="contact-block">
    <div class="person-name">Ellis Marlow</div>
    <div class="person-title">Founder</div>
    <div class="address">1875 Birchfield Rd,<br>Tulsa, OK 74105</div>
    <ul class="contact-list">
      <li>
        <svg viewBox="0 0 12 12" aria-hidden="true"><path fill="#fff" d="M3 1l2 2.5-1.2 1.3a7 7 0 0 0 3.4 3.4L8.5 7 11 9l-1.3 2C5.5 11 1 6.5 1 2.3z"/></svg>
        (555)310-2274
      </li>
      <li>
        <svg viewBox="0 0 12 12" aria-hidden="true"><rect x="0.5" y="2" width="11" height="8" fill="#fff"/><path d="M0.5 2.5L6 7l5.5-4.5" fill="none" stroke="#1446c0" stroke-width="1"/></svg>
        sales@marlowsovenworks.com
      </li>
      <li>
        <svg viewBox="0 0 12 12" aria-hidden="true"><circle cx="6" cy="6" r="5.5" fill="#fff"/><path d="M0.5 6h11M6 0.5c-2.5 3-2.5 8 0 11M6 0.5c2.5 3 2.5 8 0 11" fill="none" stroke="#1446c0" stroke-width="0.8"/></svg>
        www.marlowsovenworks.com
      </li>
    </ul>
  </div>
</section>

</body>
</html>
```